I challenge you to create Denmark's coolest roofing company website

We need to have a website created for our roofing company.

I have some pages that can be used as a starting point because there are some things we would like to have, one important thing is a roof calculator, in addition to that information about the company, pictures of tasks we have completed, links to Friendlio and Pictavoro pages.

reviews from rated, etc. should also be visible on the page.

we have lots of pictures, videos, logos,

we need to have a nice home page that is just a little cooler than the competitors.
we need to steal their customer. the page should be easy and clear but with a nice design.
an important thing is the calculator.
come up with some suggestions we are quite open as long as it is a nice design
Updates

I have made an update in the PDF file with some thoughts and wishes. The file has been uploaded.

Target Market(s)

20-60

Industry/Entity Type

carpenter - roofer

Coding

Coded - Design and coding required

Number of Pages Required

4 page

Font styles to use
Sans Serif

Colors
EB3D1F
EC4F4E
F09395
F8D3D4
FCEDEE

Requirements
Must have
• Roof calculator, nice design, easy to get around
Nice to have
• the competitors : https://mollerbyghuset.dk https://hvid-tegl.dk https://strandbyghuset.dk

```html
<!DOCTYPE html>
<html lang="en">
<head>
<meta charset="utf-8">
<title>Tagværket – Reliable Roofing Solutions</title>
<link href="https://fonts.googleapis.com/css2?family=Marcellus&family=Montserrat:wght@400;500;600;700&display=swap" rel="stylesheet">
<style>
:root{
  --red:#cc1f2d;
  --red-dark:#a8141f;
  --ink:#151515;
  --text:#333;
  --muted:#666;
  --field:#f4f4f4;
  --line:#e6e6e6;
  --navy:#222c38;
  --footer:#2a1719;
  --white:#fff;
}
*{box-sizing:border-box;margin:0;padding:0}
html,body{width:1200px;height:4474px;overflow:hidden}
body{position:relative;font-family:"Montserrat",sans-serif;color:var(--text);background:var(--white)}
.display{font-family:"Marcellus",serif;font-weight:400;color:var(--ink)}
.accent{color:var(--red)}
section,header,.topbar,footer{position:absolute;left:0;width:1200px}
.abs{position:absolute}

/* buttons */
.btn{position:absolute;display:flex;align-items:center;background:var(--red);color:var(--white);font-weight:700;font-size:13px;letter-spacing:.3px;text-transform:uppercase;padding-left:32px}
.btn .peak{position:absolute;right:-4px;bottom:0}
.btn-outline{position:absolute;display:flex;align-items:center;border:1px solid var(--ink);background:var(--white);color:var(--ink);font-weight:600;font-size:10px;padding-left:20px;text-transform:uppercase}
.btn-outline .peak{position:absolute;right:-4px;bottom:-1px}

/* top bar */
.topbar{top:0;height:17px;background:var(--red);color:var(--white);font-size:8px}
.topbar .social{left:151px;top:3px;display:flex;gap:10px}
.topbar .info{right:150px;top:3px;display:flex;gap:24px}

/* header */
header{top:17px;height:63px;background:var(--white);border-bottom:1px solid var(--line)}
.brand{display:flex;align-items:center;gap:8px;font-family:"Montserrat",sans-serif;font-weight:700;color:var(--ink)}
.brand .mark{width:14px;height:14px;background:var(--red)}
header .brand{left:151px;top:20px;font-size:20px}
.nav{left:551px;top:24px;display:flex;gap:30px;font-size:14px;font-weight:500;color:var(--ink)}
header .btn{left:850px;top:13px;width:200px;height:40px;font-size:14px;padding-left:28px}

/* hero */
.hero{top:80px;height:589px;overflow:hidden}
.hero-photo{position:absolute;left:0;top:0;width:1200px;height:589px;background:linear-gradient(90deg,#ffffff 0%,#ffffff 25%,rgba(255,255,255,.6) 45%,rgba(255,255,255,0) 62%),linear-gradient(180deg,#8fb6dc 0%,#a9c4df 35%,#9a958c 65%,#6d6a63 100%)}
.hero h1{left:151px;top:84px;font-size:54px;line-height:63px;width:420px}
.hero .lead{left:151px;top:292px;font-size:14px;font-weight:500;line-height:24px;color:var(--ink);width:420px;text-transform:uppercase}
.call{left:151px;top:390px;display:flex;align-items:center;gap:10px}
.call .ico{width:40px;height:40px;background:var(--red);display:flex;align-items:center;justify-content:center}
.call small{display:block;font-size:9px;font-weight:600;color:var(--ink)}
.call strong{display:block;font-family:"Marcellus",serif;font-weight:400;font-size:21px;color:var(--ink)}
.hero .btn{left:151px;top:458px;width:290px;height:36px}

/* estimate */
.estimate{top:669px;height:591px}
.estimate h2{top:86px;width:1200px;text-align:center;font-size:38px}
.calc{left:264px;top:173px;width:670px;height:380px;border:1px solid #efefef}
.field{position:absolute;left:20px;width:630px;height:36px;background:var(--field);display:flex;align-items:center;justify-content:space-between;padding:0 18px;font-size:10px;font-weight:500;color:var(--ink);text-transform:uppercase}
.cost{left:20px;top:262px;width:630px;display:flex;justify-content:space-between;font-family:"Marcellus",serif;font-size:23px;color:var(--ink)}
.calc .btn{left:20px;top:331px;width:290px;height:38px}

/* about */
.about{top:1260px;height:532px}
.stats{left:151px;top:98px;width:113px;border-top:1px solid var(--ink);height:298px;border-bottom:1px solid var(--ink)}
.stat{position:absolute;left:0;width:113px;text-align:center}
.stat b{display:block;font-family:"Marcellus",serif;font-weight:400;font-size:32px;color:var(--ink)}
.stat b span{color:var(--red);font-size:26px}
.stat em{display:block;font-style:normal;font-size:13px;line-height:22px;color:var(--ink);text-transform:uppercase}
.about h2{left:288px;top:56px;font-size:40px;line-height:46px}
.about p{left:288px;width:350px;font-size:10.5px;line-height:18px;color:var(--muted)}
.about .btn{left:288px;top:374px;width:220px;height:38px}
.about-photo{left:684px;top:56px;width:367px;height:381px;background:linear-gradient(180deg,#c9c7bf 0%,#b7a79c 40%,#8e8a84 70%,#6f6c68 100%)}

/* services */
.services{top:1792px;height:800px;background:linear-gradient(180deg,#26303d 0%,#232b36 60%,#2e2226 100%)}
.services h2{top:50px;width:1200px;text-align:center;font-size:38px;color:var(--white)}
.card{position:absolute;width:441px;height:217px;display:flex;background:var(--white)}
.card .img{width:217px;height:217px}
.card .body{position:relative;flex:1;padding:20px 24px}
.card h3{font-family:"Marcellus",serif;font-weight:400;font-size:18px;line-height:21px;color:var(--ink)}
.card p{margin-top:8px;font-size:9px;line-height:19px;color:var(--muted)}
.card .btn-outline{left:24px;bottom:22px;width:160px;height:28px}
.card.active .body{background:var(--red)}
.card.active h3,.card.active p{color:var(--white)}
.card.active .btn-outline{border-color:var(--white)}
.services .btn{left:151px;top:701px;width:300px;height:38px}
.arrows{display:flex;gap:8px}
.arrow{width:41px;height:41px;background:var(--red);display:flex;align-items:center;justify-content:center}
.services .arrows{left:961px;top:699px}

/* projects */
.projects{top:2592px;height:698px}
.projects h2{left:151px;top:92px;font-size:38px}
.projects .arrows{left:961px;top:96px}
.tile{position:absolute}

/* testimonials */
.testimonials{top:3290px;height:646px}
.testimonials h2{top:28px;width:1200px;text-align:center;font-size:38px}
.map{left:100px;top:160px;width:1000px;height:380px;background:radial-gradient(ellipse at center,#f6f6f6 0%,#ffffff 70%)}
.avatar{position:absolute;border-radius:50%;background:linear-gradient(160deg,#c9d3de,#7f8da0);border:3px solid var(--white);box-shadow:0 2px 8px rgba(0,0,0,.18)}
.quote-badge{left:620px;top:291px;width:34px;height:34px;border-radius:50%;background:var(--red);border:3px solid var(--white);display:flex;align-items:center;justify-content:center;color:var(--white);font-weight:700;font-size:16px}
.testimonials blockquote{position:absolute;left:300px;top:344px;width:600px;text-align:center;font-size:10.5px;line-height:18px;color:var(--muted)}
.who{left:0;top:440px;width:1200px;text-align:center;color:var(--ink)}
.who b{display:block;font-weight:500;font-size:13px}
.who small{display:block;font-weight:700;font-size:10px}

/* footer */
footer{top:3936px;height:538px;background:linear-gradient(180deg,#3a1a1d 0%,#2a1719 40%,#1f1516 100%);color:var(--white)}
footer h2{left:151px;top:62px;font-size:38px;color:var(--white)}
footer .btn{left:800px;top:65px;width:249px;height:38px}
.rule{left:151px;width:900px;height:1px;background:rgba(255,255,255,.25)}
.col{text-align:center;font-size:11px;line-height:17px}
.col h4{font-family:"Marcellus",serif;font-weight:400;font-size:18px;margin-bottom:16px}
.col li{list-style:none;margin-bottom:13px}
footer .brand{color:var(--white);font-size:32px;justify-content:center;left:450px;width:300px;top:228px}
footer .brand .mark{width:20px;height:20px}
.tagline{left:440px;top:330px;width:320px;text-align:center;font-size:11px;line-height:18px}
.socials{left:0;top:398px;width:1200px;display:flex;justify-content:center;gap:26px;font-size:10px}
.socials span{display:flex;align-items:center;gap:6px}
.socials i{width:24px;height:24px;border-radius:50%;background:var(--white);display:block}
.socials span:first-child i{background:var(--red)}
.copy{left:0;top:496px;width:1200px;text-align:center;font-size:9px}
</style>
</head>
<body>

<div class="topbar">
  <div class="abs social"><span>Chirpo</span><span>Friendlio</span><span>Pictavoro</span></div>
  <div class="abs info"><span>Strandvejen 12, 8000 Aarhus, Denmark</span><span>kontakt@tagvaerket.dk</span></div>
</div>

<header>
  <div class="abs brand"><span class="mark"></span>Tagværket</div>
  <nav class="abs nav"><span>HOME</span><span>ABOUT US</span><span>SERVICES ▾</span></nav>
  <a class="btn">CONTACT US
    <svg class="peak" width="70" height="40" viewBox="0 0 70 40"><polygon points="4,40 40,0 70,40 56,40 40,20 22,40" fill="#151515"/></svg>
  </a>
</header>

<section class="hero">
  <div class="hero-photo" role="img" aria-label="House with scaffolding during a roof renovation, company van on site"></div>
  <h1 class="abs display">Reliable <span class="accent">Roofing Solutions</span> Built To Last</h1>
  <p class="abs lead">Quality roof installations, repairs, and maintenance trusted by homeowners across</p>
  <div class="abs call">
    <span class="ico"><svg width="20" height="20" viewBox="0 0 24 24"><path d="M6.6 10.8a15.1 15.1 0 0 0 6.6 6.6l2.2-2.2a1 1 0 0 1 1-.25 11.4 11.4 0 0 0 3.6.57 1 1 0 0 1 1 1V20a1 1 0 0 1-1 1A17 17 0 0 1 3 4a1 1 0 0 1 1-1h3.5a1 1 0 0 1 1 1c0 1.25.2 2.45.57 3.6a1 1 0 0 1-.25 1z" fill="none" stroke="#fff" stroke-width="1.6"/></svg></span>
    <div><small>CALL US</small><strong>(262) 555-0148</strong></div>
  </div>
  <a class="btn">GET YOUR ROOF ESTIMATE
    <svg class="peak" width="70" height="40" viewBox="0 0 70 40"><polygon points="4,40 40,0 70,40 56,40 40,20 22,40" fill="#151515"/></svg>
  </a>
</section>

<section class="estimate">
  <h2 class="abs display">Estimate Your <span class="accent">Roof Cost</span> In Minutes</h2>
  <div class="abs calc">
    <div class="field" style="top:26px">Roof type <svg width="10" height="6"><path d="M1 1l4 4 4-4" stroke="#151515" fill="none"/></svg></div>
    <div class="field" style="top:80px">Roof size / area <svg width="10" height="6"><path d="M1 1l4 4 4-4" stroke="#151515" fill="none"/></svg></div>
    <div class="field" style="top:136px">Roof pitch / slope <svg width="10" height="6"><path d="M1 1l4 4 4-4" stroke="#151515" fill="none"/></svg></div>
    <div class="field" style="top:190px">Roof condition / extras <svg width="10" height="6"><path d="M1 1l4 4 4-4" stroke="#151515" fill="none"/></svg></div>
    <div class="abs cost"><span>Estimated Cost</span><span><span class="accent">Total</span> / $3,500</span></div>
    <a class="btn">GET A DETAILED QUOTE
      <svg class="peak" width="70" height="40" viewBox="0 0 70 40"><polygon points="4,40 40,0 70,40 56,40 40,20 22,40" fill="#151515"/></svg>
    </a>
  </div>
</section>

<section class="about">
  <div class="abs stats">
    <div class="stat" style="top:30px"><b>10k <span>+</span></b><em>Lorem ipsum<br>dolor</em></div>
    <div class="stat" style="top:172px"><b>10k <span>+</span></b><em>Lorem ipsum<br>dolor</em></div>
  </div>
  <h2 class="abs display">About The<br><span class="accent">Tagværket</span></h2>
  <p class="abs" style="top:180px">Lorem Ipsum Dolor Sit Amet Consectetur. Velit Tortor Molestie Praesent Est Eget Etiam Consequat. Nibh Tristique Vel Ut Hac Odio Ut Tempor Turpis. Et Penatibus Ornare Neque Hendrerit Mauris Rhoncus Lectus. Lectus Nisl Quam Viverra Amet Gravida In.</p>
  <p class="abs" style="top:284px">Lorem Ipsum Dolor Sit Amet Consectetur. Velit Tortor Molestie Praesent Est Eget Etiam Consequat. Nibh Tristique Vel Ut Hac Odio Ut Tempor Turpis.</p>
  <a class="btn">DISCOVER MORE
    <svg class="peak" width="70" height="40" viewBox="0 0 70 40"><polygon points="4,40 40,0 70,40 56,40 40,20 22,40" fill="#151515"/></svg>
  </a>
  <div class="abs about-photo" role="img" aria-label="Company trailer parked in front of a brick house with scaffolding"></div>
</section>

<section class="services">
  <h2 class="abs display">Our Roofing Services We Offered</h2>
  <div class="card active" style="left:151px;top:162px">
    <div class="img" role="img" aria-label="Roof installation with new rafters and membrane" style="background:linear-gradient(160deg,#b8c6d3,#4d4a47)"></div>
    <div class="body"><h3>Roof Installation</h3><p>Lorem Ipsum Dolor Sit Amet Consectetur. Non Scelerisque Arcu Venenatis Fames. Mollis Donec Velit Id Facilisi Morbi Suspendisse Eu Nam. Et Vel Mauris Varius Habitant. At Enim.</p>
      <a class="btn-outline">DISCOVER MORE<svg class="peak" width="48" height="30" viewBox="0 0 48 30"><polygon points="2,30 28,0 48,30 38,30 28,14 14,30" fill="#fff"/></svg></a></div>
  </div>
  <div class="card" style="left:610px;top:162px">
    <div class="img" role="img" aria-label="Roof repair with tiles removed under blue sky" style="background:linear-gradient(170deg,#6d9ed0,#c9c0ad 60%,#6a6459)"></div>
    <div class="body"><h3>Roof Repair</h3><p>Lorem Ipsum Dolor Sit Amet Consectetur. Non Scelerisque Arcu Venenatis Fames. Mollis Donec Velit Id Facilisi Morbi Suspendisse Eu Nam. Et Vel Mauris Varius Habitant. At Enim.</p>
      <a class="btn-outline">DISCOVER MORE<svg class="peak" width="48" height="30" viewBox="0 0 48 30"><polygon points="2,30 28,0 48,30 38,30 28,14 14,30" fill="#151515"/></svg></a></div>
  </div>
  <div class="card" style="left:151px;top:405px">
    <div class="img" role="img" aria-label="Roof maintenance on a slate roof with scaffolding" style="background:linear-gradient(160deg,#aac0d4,#3f4a55 55%,#2d333a)"></div>
    <div class="body"><h3>Roof Maintenance</h3><p>Lorem Ipsum Dolor Sit Amet Consectetur. Non Scelerisque Arcu Venenatis Fames. Mollis Donec Velit Id Facilisi Morbi Suspendisse Eu Nam. Et Vel Mauris Varius Habitant. At Enim.</p>
      <a class="btn-outline">DISCOVER MORE<svg class="peak" width="48" height="30" viewBox="0 0 48 30"><polygon points="2,30 28,0 48,30 38,30 28,14 14,30" fill="#151515"/></svg></a></div>
  </div>
  <div class="card" style="left:610px;top:405px">
    <div class="img" role="img" aria-label="Roof replacement with battens over dark underlay" style="background:linear-gradient(160deg,#8a7358,#3a3c40 60%,#2a2b2e)"></div>
    <div class="body"><h3>Roof Replacement / Renovation</h3><p>Lorem Ipsum Dolor Sit Amet Consectetur. Non Scelerisque Arcu Venenatis Fames. Mollis Donec Velit Id Facilisi Morbi Suspendisse Eu Nam.</p>
      <a class="btn-outline">DISCOVER MORE<svg class="peak" width="48" height="30" viewBox="0 0 48 30"><polygon points="2,30 28,0 48,30 38,30 28,14 14,30" fill="#151515"/></svg></a></div>
  </div>
  <a class="btn">DISCOVER MORE SERVICES
    <svg class="peak" width="70" height="40" viewBox="0 0 70 40"><polygon points="4,40 40,0 70,40 56,40 40,20 22,40" fill="#fff"/></svg>
  </a>
  <div class="abs arrows">
    <span class="arrow"><svg width="12" height="14"><path d="M9 1L3 7l6 6" stroke="#fff" stroke-width="2" fill="none"/></svg></span>
    <span class="arrow"><svg width="12" height="14"><path d="M3 1l6 6-6 6" stroke="#fff" stroke-width="2" fill="none"/></svg></span>
  </div>
</section>

<section class="projects">
  <h2 class="abs display">Our Recent <span class="accent">Projects</span></h2>
  <div class="abs arrows">
    <span class="arrow"><svg width="12" height="14"><path d="M9 1L3 7l6 6" stroke="#fff" stroke-width="2" fill="none"/></svg></span>
    <span class="arrow"><svg width="12" height="14"><path d="M3 1l6 6-6 6" stroke="#fff" stroke-width="2" fill="none"/></svg></span>
  </div>
  <div class="tile" role="img" aria-label="Finished house with new grey roof" style="left:151px;top:201px;width:292px;height:278px;background:linear-gradient(180deg,#8db4dc 0%,#a9bdd0 35%,#6b6b6b 55%,#d8d2c4 80%,#6f8a5a 100%)"></div>
  <div class="tile" role="img" aria-label="New orange clay tile roof" style="left:151px;top:493px;width:292px;height:146px;background:linear-gradient(160deg,#5c5853,#d1642e 40%,#b5521f)"></div>
  <div class="tile" role="img" aria-label="Dark metal tile roof ridge seen from scaffold" style="left:455px;top:201px;width:292px;height:438px;background:linear-gradient(180deg,#c9d1d8 0%,#b9c0c6 30%,#4a4d52 55%,#6a6259 100%)"></div>
  <div class="tile" role="img" aria-label="Slate roof with ladder" style="left:759px;top:201px;width:292px;height:146px;background:linear-gradient(160deg,#9aa1a6,#5e6469)"></div>
  <div class="tile" role="img" aria-label="Close view of red ridge tiles against the sky" style="left:759px;top:361px;width:292px;height:278px;background:linear-gradient(180deg,#7fb3e6 0%,#9cc4ea 30%,#c45a2c 55%,#a9421c 100%)"></div>
</section>

<section class="testimonials">
  <h2 class="abs display">Hear From Our <span class="accent">Happy Customers</span></h2>
  <div class="abs map" role="img" aria-label="Faint dotted world map background"></div>
  <div class="avatar" role="img" aria-label="Customer portrait" style="left:236px;top:211px;width:60px;height:60px"></div>
  <div class="avatar" role="img" aria-label="Customer portrait" style="left:390px;top:232px;width:46px;height:46px"></div>
  <div class="avatar" role="img" aria-label="Featured customer portrait" style="left:549px;top:204px;width:100px;height:100px"></div>
  <div class="abs quote-badge">”</div>
  <div class="avatar" role="img" aria-label="Customer portrait" style="left:736px;top:218px;width:46px;height:46px"></div>
  <div class="avatar" role="img" aria-label="Customer portrait" style="left:941px;top:211px;width:60px;height:60px"></div>
  <div class="avatar" role="img" aria-label="Customer portrait" style="left:163px;top:352px;width:46px;height:46px"></div>
  <div class="avatar" role="img" aria-label="Customer portrait" style="left:991px;top:366px;width:46px;height:46px"></div>
  <div class="avatar" role="img" aria-label="Customer portrait" style="left:291px;top:437px;width:60px;height:60px"></div>
  <div class="avatar" role="img" aria-label="Customer portrait" style="left:835px;top:437px;width:60px;height:60px"></div>
  <blockquote>Lorem Ipsum Dolor Sit Amet Consectetur. Sit Nulla Lacus Ipsum Lectus Vitae Ut Nulla Ipsum Neque. Leo Elementum Orci Tincidunt Pulvinar Risus. Eu Pulvinar Nisl Mus Ipsum Venenatis Eu Integer Nunc Tincidunt. Etiam Nulla In Facilisi Etiam Eget Cursus Massa Amet Consequat. In Pretium Eu Volutpat Malesuada Sit Mi Dictum Suscipit. Eu Porttitor Rhoncus Est Nunc Sollicitudin</blockquote>
  <div class="abs who"><b>JONAS HOLM</b><small>Co - Founder</small></div>
</section>

<footer>
  <h2 class="abs display">Ready To Upgrade Your Roof?</h2>
  <a class="btn">CALCULATE NOW
    <svg class="peak" width="70" height="40" viewBox="0 0 70 40"><polygon points="4,40 40,0 70,40 56,40 40,20 22,40" fill="#fff"/></svg>
  </a>
  <div class="abs rule" style="top:146px"></div>
  <div class="abs col" style="left:126px;top:216px;width:200px">
    <h4>Contact Us</h4>
    <p>kontakt@tagvaerket.dk</p>
    <p style="margin-top:12px">Strandvejen 12, 8000<br>Aarhus, Denmark</p>
    <p style="margin-top:12px">(262) 555-0148</p>
  </div>
  <div class="abs brand"><span class="mark"></span>Tagværket</div>
  <p class="abs tagline">Lorem Ipsum Dolor Sit Amet Consectetur. Leo Ornare Purus Id Ut Sem.</p>
  <div class="abs col" style="left:908px;top:216px;width:200px">
    <h4>Support</h4>
    <ul><li>Lorem Ipsum</li><li>Lorem</li><li>Lorem Ipsum</li><li>Lorem Ipsum</li></ul>
  </div>
  <div class="abs socials"><span><i></i>Friendlio</span><span><i></i>Pictavoro</span><span><i></i>Chirpo</span></div>
  <div class="abs rule" style="top:484px"></div>
  <p class="abs copy">© 2025 All Rights Reserved.</p>
</footer>

</body>
</html>
```